Roof wash and Gutter Cleaning

Would like to see our colors and logo incorporated into design along with phone number and before/after picture(s). We use a non pressure softwash process we use unlike high pressure. We are a exterior cleaning company that likes to set our standards high with safe methods to cleaning the everyday surfaces on homes.
“Serving the Tri-State Area”
A list of our services:
House washing
Shingle and metal roof washing
Deck cleaning
Window cleaning
Concrete cleaning
Gutter cleaning
514-362-0917
We do not need the address section as these will be more for our meet and greets. As well handed out as clipped door  postcards.

Shingle roof wash and gutter cleaning

```html
<!DOCTYPE html>
<html lang="en">
<head>
<meta charset="utf-8">
<title>Summit Exterior Cleaning – Roll-up Banner</title>
<link href="https://fonts.googleapis.com/css2?family=Bebas+Neue&family=Poppins:wght@600;700;800&display=swap" rel="stylesheet">
<style>
  :root{
    --blue:#0a4fb8;
    --blue-bright:#1c6fe0;
    --navy:#0a2a8a;
    --lime:#b6e01c;
    --lime-dark:#8fbf0e;
    --white:#ffffff;
    --page:#e6e6e6;
  }
  *{margin:0;padding:0;box-sizing:border-box}
  html,body{width:1200px;height:1200px;overflow:hidden;background:var(--page)}
  .banner{position:absolute;left:351px;top:20px;width:498px;height:1160px;overflow:hidden;
    background:linear-gradient(180deg,var(--blue-bright) 0%,var(--blue) 18%,var(--blue) 100%);
    font-family:"Poppins",sans-serif;color:var(--white)}
  .headline{position:absolute;top:44px;left:0;width:100%;text-align:center;
    font-family:"Bebas Neue",sans-serif;font-size:58px;line-height:1;letter-spacing:.5px;
    text-shadow:0 2px 4px rgba(0,0,0,.35)}
  .subhead{position:absolute;top:102px;left:0;width:100%;text-align:center;
    font-family:"Bebas Neue",sans-serif;font-size:40px;line-height:1;color:var(--lime);
    text-shadow:0 2px 3px rgba(0,0,0,.3)}
  .hero-photo{position:absolute;left:0;top:262px;width:100%;height:130px;
    background:linear-gradient(90deg,#f4f6f7 0%,#e9eef0 45%,#c9d3b4 70%,#8c9a5e 100%)}
  .swoosh{position:absolute;left:0;top:200px;width:498px;height:200px}
  .logo-badge{position:absolute;left:137px;top:152px;width:214px;height:214px;border-radius:50%;
    background:var(--white);border:6px solid var(--blue);box-shadow:0 4px 10px rgba(0,0,0,.3), 8px 10px 0 -2px var(--lime);
    display:flex;flex-direction:column;align-items:center;justify-content:center;gap:6px}
  .logo-name{font-size:40px;font-weight:800;color:var(--blue);line-height:1}
  .logo-tag{font-size:8px;font-weight:600;color:var(--blue);opacity:.8}
  .results{position:absolute;left:0;top:390px;width:100%;height:281px;background:var(--navy);
    display:grid;grid-template-columns:1fr 1fr;grid-template-rows:110px 27px 118px 26px;gap:0 2px}
  .photo{display:block}
  .roof-grey-before{background:linear-gradient(160deg,#7d7a72 0%,#6b6659 45%,#8a6b4a 70%,#58604a 100%)}
  .roof-grey-after{background:linear-gradient(160deg,#9a968c 0%,#8d897e 50%,#6f7466 100%)}
  .roof-red-before{background:linear-gradient(160deg,#8b5a44 0%,#7a5a46 50%,#8c8170 75%,#6c6a5c 100%)}
  .roof-red-after{background:linear-gradient(160deg,#b0634a 0%,#a8573f 55%,#b9bcb8 85%,#8a8d80 100%)}
  .label{background:var(--blue);display:flex;align-items:center;justify-content:center;
    font-weight:800;font-size:18px;letter-spacing:.5px}
  .scene-photo{position:absolute;left:0;top:671px;width:100%;height:320px;
    background:linear-gradient(180deg,#c9cc8a 0%,#8fa24e 30%,#6f8a3a 55%,#5f7e8e 80%,#3b7fc0 100%)}
  .area-box{position:absolute;left:59px;top:692px;width:380px;height:93px;border-radius:14px;
    background:linear-gradient(180deg,var(--blue-bright),var(--blue));border:3px solid var(--lime);
    text-align:center;color:var(--lime);font-weight:800;box-shadow:0 3px 8px rgba(0,0,0,.35)}
  .area-small{font-size:26px;line-height:1;margin-top:12px;letter-spacing:-.5px}
  .area-large{font-size:38px;line-height:1;margin-top:2px;letter-spacing:-1.5px}
  .services{position:absolute;left:47px;top:800px;width:403px;height:131px;border-radius:16px;
    background:linear-gradient(180deg,var(--blue-bright),var(--blue));border:3px solid var(--lime);
    padding:14px 0 0 30px;display:grid;grid-template-columns:176px 1fr;column-gap:0;
    font-family:"Bebas Neue",sans-serif;font-size:21px;line-height:25px;color:var(--lime);
    box-shadow:0 3px 8px rgba(0,0,0,.35)}
  .services ul{list-style:none}
  .services li{position:relative;padding-left:30px}
  .services li::before{content:"";position:absolute;left:2px;top:6px;width:13px;height:13px;border-radius:50%;background:var(--white)}
  .contact{position:absolute;left:0;top:980px;width:100%;height:180px;background:var(--navy)}
  .call-pill{position:absolute;left:43px;top:951px;width:413px;height:55px;border-radius:28px;
    background:var(--lime);color:var(--navy);font-weight:800;font-size:23px;
    display:flex;align-items:center;justify-content:center;letter-spacing:-.3px}
  .call-pill::after{content:"";position:absolute;left:196px;bottom:-12px;border:10px solid transparent;border-top:12px solid var(--lime);border-bottom:0}
  .phone{position:absolute;left:0;top:1030px;width:100%;display:flex;align-items:center;justify-content:center;gap:6px;
    font-weight:800;font-size:44px;letter-spacing:-.5px;line-height:1}
  .phone svg{width:44px;height:44px}
  .web{position:absolute;left:0;top:1098px;width:100%;text-align:center;font-weight:700;font-size:17px;letter-spacing:.2px}
  .web span{color:var(--lime)}
</style>
</head>
<body>
<main class="banner">
  <h1 class="headline">Exterior Cleaning</h1>
  <h2 class="subhead">&amp; Maintenance</h2>

  <div class="hero-photo" role="img" aria-label="Photo of a clean white home exterior with sunlit greenery"></div>
  <svg class="swoosh" viewBox="0 0 498 200" aria-hidden="true">
    <path d="M0 60 Q120 30 240 20 Q360 30 498 60 L498 90 Q360 55 240 50 Q120 55 0 100 Z" fill="#0a2a8a"/>
    <path d="M0 100 Q120 55 240 50 Q360 55 498 90 L498 118 Q360 70 240 70 Q120 75 0 122 Z" fill="#b6e01c"/>
  </svg>

  <div class="logo-badge">
    <div class="logo-name">Summit</div>
    <div class="logo-tag">Exterior Cleaning &amp; Maintenance Co.</div>
  </div>

  <section class="results">
    <div class="photo roof-grey-before" role="img" aria-label="Grey shingle roof with debris and stains before washing"></div>
    <div class="photo roof-grey-after" role="img" aria-label="Grey shingle roof clean after soft washing"></div>
    <div class="label">BEFORE</div>
    <div class="label">AFTER</div>
    <div class="photo roof-red-before" role="img" aria-label="Red shingle roof with leaf-filled valley before cleaning"></div>
    <div class="photo roof-red-after" role="img" aria-label="Red shingle roof bright and clean after washing"></div>
    <div class="label">BEFORE</div>
    <div class="label">AFTER</div>
  </section>

  <div class="scene-photo" role="img" aria-label="Countryside landscape at sunset with tiled roof and pool"></div>

  <div class="area-box">
    <div class="area-small">SERVING THE</div>
    <div class="area-large">Tri-State Area”</div>
  </div>

  <div class="services">
    <ul>
      <li>House Washing</li>
      <li>Shingle and<br>Metal Roof Washing</li>
      <li>Deck Cleaning</li>
    </ul>
    <ul>
      <li>Window Cleaning</li>
      <li>Concrete Cleaning</li>
      <li>Gutter Cleaning</li>
    </ul>
  </div>

  <div class="contact"></div>
  <div class="call-pill">PLEASE CALL US ANYTIME</div>

  <div class="phone">
    <svg viewBox="0 0 44 44" aria-hidden="true">
      <circle cx="22" cy="22" r="19" fill="none" stroke="#b6e01c" stroke-width="4"/>
      <circle cx="22" cy="22" r="14" fill="#b6e01c"/>
      <path d="M16 14c1-1 2-1 3 0l2 3c.5 1 0 2-1 2.5-.5.3-.5 1 0 1.8 1 1.6 2 2.6 3.5 3.5.8.5 1.5.5 1.8 0 .5-1 1.5-1.5 2.5-1l3 2c1 1 1 2 0 3-2 2-5 2-8 0-3-2-6-5-7.5-8-1.5-3-1.3-5.5.7-7.8z" fill="#0a2a8a"/>
    </svg>
    <span>514-362-0917</span>
  </div>
  <div class="web">SUMMITEXTCLEANING.COM/<span>PAGE</span></div>
</main>
</body>
</html>
```